Velmora Junior Reading & Counting Drive

Development of the (VJRCD) website. The Velmora Junior Reading and Counting Drive (VJRCD) is a Velmora Office of Schooling Project running in approximately 810 participating Gauteng Primary Schools. The project goals are to improve Language and Mathematics scores in participating schools.
The colors should be the same colors as Velmora Schooling office colors ( see logos)

Try bring in human element - this project is about improving literacy and numeracy levels of marginalized primary school children.

Target Market(s)

Education sector and general public

Industry/Entity Type

School

Requirements
Must have
• The primary navigation of the site must always be displayed on each page.
? Each section must have a main page where visitors can navigate to the sub items under the relevant section.
? The overall design concept for the website must be optimised in terms of brand identity, accessibility, usability and content distribution. Colours and images must be chosen according to VJRCD’s corporate identity requirements.
? The VJRCD’s logo should be present on the homepage and visible at all times during a person’s visit.

```html
<!DOCTYPE html>
<html lang="en">
<head>
<meta charset="utf-8">
<title>Velmora Junior Reading &amp; Counting Drive</title>
<link href="https://fonts.googleapis.com/css2?family=Arimo:wght@400;700&family=Cabin:wght@400;500;600&display=swap" rel="stylesheet">
<style>
:root{
  --green:#9bb81e;
  --orange:#f9a100;
  --red:#c9343a;
  --cyan:#1aa3c4;
  --navy:#2a3a8c;
  --footer-bg:#ebeaea;
  --ink:#333;
  --white:#fff;
}
*{margin:0;padding:0;box-sizing:border-box}
html,body{width:914px;height:1200px;overflow:hidden;background:var(--white)}
body{position:relative;font-family:"Arimo",Arial,sans-serif}

.hero{position:absolute;left:0;top:0;width:914px;height:445px;
  background:linear-gradient(100deg,#6b4a3a 0%,#b58e6a 30%,#e6d8c4 55%,#d9c2a8 75%,#8a6a56 100%)}
.hero-title{position:absolute;left:34px;top:250px;color:var(--white);font-weight:700;font-size:37px;line-height:42px;text-shadow:1px 1px 3px rgba(0,0,0,.45)}

.brand{position:absolute;left:6px;top:0;width:305px;height:118px;background:var(--white);box-shadow:0 2px 6px rgba(0,0,0,.25);display:flex;align-items:center;padding-left:30px;gap:12px}
.brand-mark{width:34px;height:34px;background:var(--navy)}
.brand-name{font-family:"Cabin",sans-serif;font-weight:600;font-size:17px;color:var(--navy);line-height:20px}

.nav{position:absolute;top:0;left:372px;display:flex;list-style:none}
.nav li{color:var(--white);font-weight:700;font-size:17px;display:flex;align-items:center;justify-content:center;text-align:center;line-height:17px}
.nav .home{background:var(--green);width:134px;height:93px}
.nav .about{background:var(--orange);width:135px;height:80px}
.nav .team{background:var(--red);width:126px;height:80px}
.nav .contact{background:var(--cyan);width:147px;height:80px}

.card{position:absolute;top:456px;height:455px;color:var(--white);font-family:"Cabin",sans-serif}
.card-green{left:10px;width:287px;background:var(--green)}
.card-orange{left:315px;width:286px;background:var(--orange)}
.card-red{left:615px;width:286px;background:var(--red)}
.card h2{font-weight:500;font-size:27px;line-height:35px;letter-spacing:.5px;position:absolute;left:21px;top:24px}
.card h2 .big{font-size:40px;line-height:44px}
.card-red h2{letter-spacing:1px}
.card-red h2 .spaced{letter-spacing:9px;font-size:30px}
.intro{position:absolute;left:26px;top:110px;width:230px;font-size:13px;line-height:19px;text-transform:uppercase}
.links{position:absolute;left:27px;top:209px;width:230px;list-style:none;border-top:1px solid rgba(255,255,255,.7)}
.links li{display:flex;align-items:center;gap:8px;min-height:46px;border-bottom:1px solid rgba(255,255,255,.7);font-family:"Arimo",sans-serif;font-weight:700;font-size:11.5px;line-height:16px;text-transform:uppercase}
.links li:first-child{min-height:56px}
.links svg{flex:none}
.media{position:absolute;left:15px;top:107px;width:256px;height:155px}
.media-blocks{background:linear-gradient(90deg,#f4f4f6,#e9e6e4)}
.media-tree{left:22px;top:105px;width:247px;height:243px;background:linear-gradient(180deg,#ffffff,#e4e8f3)}
.body-text{position:absolute;left:19px;top:280px;width:250px;font-size:13px;line-height:19.5px}
.read-more{position:absolute;left:30px;bottom:30px;background:var(--white);font-size:17px;font-weight:500;padding:7px 13px;text-transform:uppercase}
.card-green .read-more{color:var(--green)}
.card-orange .read-more{left:18px;bottom:26px;color:var(--orange)}
.card-red .read-more{left:21px;bottom:26px;color:var(--red)}

.footer{position:absolute;left:0;top:928px;width:914px;height:217px;background:var(--footer-bg)}
.footer-links{position:absolute;top:32px;list-style:none;font-weight:700;font-size:12px;color:var(--ink)}
.footer-links li{height:24px}
.col-a{left:69px}.col-b{left:268px}
.office{position:absolute;left:507px;top:93px;color:var(--ink)}
.office h3{font-size:18px;font-weight:700;margin-bottom:3px}
.office p{font-size:11.5px;line-height:24px}
.footer-art{position:absolute;left:716px;top:42px;width:160px;height:150px;background:linear-gradient(180deg,#ebeaea,#d7dbe8)}

.bottom-bar{position:absolute;left:0;top:1145px;width:914px;height:55px;background:var(--cyan)}
.social{position:absolute;left:20px;top:19px;display:flex;gap:7px}
.social span{width:20px;height:20px;border-radius:50%;background:#c9cfd3}
.copyright{position:absolute;right:22px;top:24px;color:var(--white);font-size:9.5px}
</style>
</head>
<body>
  <div class="hero" role="img" aria-label="Photo of a smiling schoolboy raising his hand in a classroom"></div>
  <h1 class="hero-title">Velmora Junior<br>Reading &amp;<br>Counting Drive</h1>

  <div class="brand">
    <span class="brand-mark"></span>
    <span class="brand-name">VELMORA PROVINCE</span>
  </div>

  <ul class="nav">
    <li class="home">HOME</li>
    <li class="about">ABOUT<br>VJRCD</li>
    <li class="team">TEAM</li>
    <li class="contact">CONTACT</li>
  </ul>

  <section class="card card-green">
    <h2>WHAT IS<br>OUR STRATEGY?</h2>
    <p class="intro">Laroeet dolore magna orem ipsum dolor ser dadpiscing elit, sed diam nonummy nibh tincidumt ut laroet</p>
    <ul class="links">
      <li><svg width="27" height="27" viewBox="0 0 27 27"><circle cx="13.5" cy="13.5" r="13" fill="#e9eedb"/><path d="M11 8.5l6 5-6 5z" fill="#9bb81e"/></svg>Research that benefits children</li>
      <li><svg width="27" height="27" viewBox="0 0 27 27"><circle cx="13.5" cy="13.5" r="13" fill="#e9eedb"/><path d="M11 8.5l6 5-6 5z" fill="#9bb81e"/></svg>Programs for educators</li>
      <li><svg width="27" height="27" viewBox="0 0 27 27"><circle cx="13.5" cy="13.5" r="13" fill="#e9eedb"/><path d="M11 8.5l6 5-6 5z" fill="#9bb81e"/></svg>Dynamic classrooms</li>
    </ul>
    <span class="read-more">Read more</span>
  </section>

  <section class="card card-orange">
    <h2>OUR<br><span class="big">IMPACT</span></h2>
    <div class="media media-blocks" role="img" aria-label="Photo of a child's hand arranging coloured number blocks into a sum"></div>
    <p class="body-text">Laoreet dolore magna.orem ipsum dolor ser adipiscing elit, sed diam nonummy nibh euismod tincidunt ut laoreet dolore set.sit amet consectetuer Aadipiscing ed diam nonummy.</p>
    <span class="read-more">Read more</span>
  </section>

  <section class="card card-red">
    <h2>WHAT IS<br><span class="spaced">VJRCD</span></h2>
    <div class="media media-tree" role="img" aria-label="Illustration of a tree made of letters and numbers"></div>
    <span class="read-more">Read more</span>
  </section>

  <footer class="footer">
    <ul class="footer-links col-a">
      <li>Projects</li><li>Latest News</li><li>Structure</li><li>Goals</li><li>Consultants</li><li>Service Providers</li><li>District Involvements</li>
    </ul>
    <ul class="footer-links col-b">
      <li>Projects</li><li>Latest News</li><li>Structure</li><li>Goals</li><li>Consultants</li><li>Service Providers</li><li>District Involvements</li>
    </ul>
    <div class="office">
      <h3>Velmora Province</h3>
      <p>Republic of Velmora</p>
      <p>xxx-xxxx-xxxx-xxxxxx</p>
      <p>xxxx-xxxxxx-xxxx</p>
    </div>
    <div class="footer-art" role="img" aria-label="Small illustration of a tree made of letters and numbers"></div>
  </footer>

  <div class="bottom-bar">
    <div class="social"><span></span><span></span><span></span></div>
    <p class="copyright">Copyright © 2012 Brightline Studio Pty Ltd</p>
  </div>
</body>
</html>
```